Northfield Builders Guild Business card

We are looking for a new business card design with photo included.
Our business is a nonprofit construction contractor membership organization. We offer business education, assist with business setup and licensing, provide safety training, and provide a member directory.
URL: www.brickwayguildnetwork.org
Color code:
CMYK: 0 cyan, 42 magenta, 100 yellow, 0 black for Print.
Hexidecimal: #FF9900
RGB: R 255; G 153; B 0

```html
<!DOCTYPE html>
<html lang="en">
<head>
<meta charset="utf-8">
<title>Northfield Builders Guild – Business Card</title>
<link rel="stylesheet" href="https://fonts.googleapis.com/css2?family=Montserrat:wght@500;600;800&display=swap">
<style>
  :root {
    --orange: #FF9900;
    --ink: #1f1f1f;
    --card: #f5f4f4;
    --stage: #2b2b2b;
  }
  * { box-sizing: border-box; margin: 0; padding: 0; }
  html, body { width: 1200px; height: 1015px; overflow: hidden; }
  body {
    background: var(--stage);
    font-family: "Montserrat", Arial, sans-serif;
    color: var(--ink);
    position: relative;
  }
  .card {
    position: absolute;
    left: 230px;
    width: 740px;
    height: 423px;
    background: var(--card);
    border-radius: 4px;
  }
  .card--front { top: 55px; }
  .card--back { top: 537px; }

  /* front */
  .front-wordmark {
    position: absolute;
    left: 0; right: 0; top: 120px;
    text-align: center;
    font-weight: 800;
    font-size: 46px;
    line-height: 1.05;
    letter-spacing: 1px;
    color: var(--ink);
  }
  .front-url {
    position: absolute;
    left: 0; right: 0; top: 310px;
    text-align: center;
    font-weight: 800;
    font-size: 22px;
    letter-spacing: 1.5px;
    color: var(--ink);
  }

  /* back */
  .back-wordmark {
    position: absolute;
    left: 52px; top: 52px;
    font-weight: 800;
    font-size: 32px;
    line-height: 1.05;
    letter-spacing: 0.5px;
    color: var(--ink);
  }
  .contact-list {
    position: absolute;
    left: 52px; top: 188px;
    list-style: none;
    font-weight: 500;
    font-size: 19px;
    line-height: 30px;
  }
  .contact-list li { display: flex; align-items: center; gap: 10px; }
  .contact-list .icon {
    width: 22px; height: 22px; flex: none;
    border-radius: 50%;
    background: var(--orange);
    display: flex; align-items: center; justify-content: center;
  }
  .contact-list .address { padding-left: 32px; line-height: 26px; margin-top: 4px; }
  .person {
    position: absolute;
    right: 52px; top: 72px;
    text-align: right;
  }
  .person-name {
    font-weight: 800;
    font-size: 30px;
    color: var(--orange);
    letter-spacing: 0.5px;
  }
  .person-title {
    font-weight: 600;
    font-size: 18px;
    letter-spacing: 1px;
    margin-top: 2px;
  }
  .back-url {
    position: absolute;
    right: 52px; bottom: 70px;
    font-weight: 800;
    font-size: 21px;
    color: var(--orange);
    letter-spacing: 0.5px;
  }
</style>
</head>
<body>
  <section class="card card--front">
    <p class="front-wordmark">NORTHFIELD<br>BUILDERS GUILD</p>
    <p class="front-url">www.brickwayguildnetwork.org</p>
  </section>

  <section class="card card--back">
    <p class="back-wordmark">NORTHFIELD<br>BUILDERS GUILD</p>

    <div class="person">
      <p class="person-name">DANIEL WHITAKER</p>
      <p class="person-title">MANAGING DIRECTOR</p>
    </div>

    <ul class="contact-list">
      <li><span class="icon"><svg width="12" height="12" viewBox="0 0 24 24"><path fill="#fff" d="M6.6 10.8a15 15 0 0 0 6.6 6.6l2.2-2.2c.3-.3.7-.4 1-.2 1.1.4 2.3.6 3.6.6.6 0 1 .4 1 1V20c0 .6-.4 1-1 1A17 17 0 0 1 3 4c0-.6.4-1 1-1h3.5c.6 0 1 .4 1 1 0 1.3.2 2.5.6 3.6.1.3 0 .7-.2 1z"/></svg></span>(555) 214-7830</li>
      <li><span class="icon"><svg width="10" height="12" viewBox="0 0 20 24"><rect x="3" y="1" width="14" height="22" rx="2" fill="none" stroke="#fff" stroke-width="2.5"/></svg></span>800-555-0147</li>
      <li><span class="icon"><svg width="12" height="12" viewBox="0 0 24 24"><rect x="6" y="3" width="12" height="5" fill="#fff"/><rect x="3" y="9" width="18" height="8" rx="1" fill="#fff"/><rect x="7" y="15" width="10" height="6" fill="#fff"/></svg></span>555.302.6614</li>
      <li><span class="icon"><svg width="12" height="10" viewBox="0 0 24 18"><rect x="1" y="1" width="22" height="16" fill="none" stroke="#fff" stroke-width="2.5"/><path d="M1 1l11 9 11-9" fill="none" stroke="#fff" stroke-width="2.5"/></svg></span>hello@nbguild.org</li>
      <li class="address">2400 Alder Ridge Rd<br>Suite #210, Millbrook<br>OR 97000</li>
    </ul>

    <p class="back-url">www.brickwayguildnetwork.org</p>
  </section>
</body>
</html>
```